Tights Color Chart

We Need for a Webshop 3 or 4 different Color Charts to see the Colors of the Tights.

1 Color Chart only with this Colors: black/schwarz, white/weiss,
naturel/natur.

The other 3 or 4 Charts up to your Design!

Total 54 Colors.

The Language must be in English and German.
Each single Color Chart should have rounded Corners see attachment.

Thank you in advance
BEN

Target Market(s)

Woman, Webshop

Requirements
Must have
• the right Colors, English and German, for the Webshop

```html
<!DOCTYPE html>
<html lang="en">
<head>
<meta charset="UTF-8">
<title>Tights Color Chart</title>
<link rel="stylesheet" href="https://fonts.googleapis.com/css2?family=Open+Sans:wght@400;700&display=swap">
<style>
  :root {
    --paper: #ffffff;
    --ink: #111111;
    --bady-pink: #e3d8dc;
    --pink: #e1c4d2;
    --orchidea: #d57fa8;
    --crocus: #c84e9c;
    --lila: #c5aed3;
    --iris: #8b68aa;
    --azalea: #8b4f8d;
    --mulberry: #884268;
    --orange: #d38134;
    --lipstic: #ad4656;
    --rosso: #ae4848;
    --salmon: #cd857f;
    --beige: #a47f63;
    --nugat: #87695b;
    --kakao: #6d4c4a;
    --berry: #7d566e;
    --kiwi: #e1e99c;
    --lipstic-green: #7bc47a;
    --verde: #8fc5b6;
    --grass: #44a058;
    --lazur: #69c8c6;
    --turquoise: #24bbc2;
    --lagoon: #34bbb0;
    --jeans: #51718c;
  }
  * { box-sizing: border-box; margin: 0; padding: 0; }
  html, body {
    width: 823px; height: 1200px; overflow: hidden;
    background: var(--paper);
    font-family: "Open Sans", Arial, sans-serif;
    color: var(--ink);
  }
  .chart { position: relative; width: 823px; height: 1200px; }
  .chart-title {
    position: absolute; top: 73px; left: 0; width: 768px;
    text-align: center; font-size: 15px; font-weight: 700; letter-spacing: 0.3px;
  }
  .swatch-grid {
    position: absolute; left: 127px; top: 142px;
    display: grid;
    grid-template-columns: 116px 116px 116px 116px;
    column-gap: 31px;
    grid-template-rows: 161px 155px 162px 169px 163px auto;
  }
  .swatch-card { width: 116px; text-align: center; }
  .swatch {
    width: 116px; height: 75px; border-radius: 11px;
    background: var(--tone);
  }
  .color-name-en { margin-top: 17px; font-size: 15.5px; font-weight: 700; line-height: 20px; }
  .color-name-de { font-size: 15.5px; font-weight: 400; line-height: 21px; }
  .color-name-de.is-bold { font-weight: 700; }
</style>
</head>
<body>
<main class="chart">
  <h1 class="chart-title">TIGHTS COLOR CHART</h1>
  <section class="swatch-grid">
    <div class="swatch-card"><div class="swatch" style="--tone: var(--bady-pink)"></div><p class="color-name-en">bady pink</p><p class="color-name-de is-bold">bady rosa</p></div>
    <div class="swatch-card"><div class="swatch" style="--tone: var(--pink)"></div><p class="color-name-en">pink</p><p class="color-name-de">rosa</p></div>
    <div class="swatch-card"><div class="swatch" style="--tone: var(--orchidea)"></div><p class="color-name-en">orchidea</p><p class="color-name-de">orchidea</p></div>
    <div class="swatch-card"><div class="swatch" style="--tone: var(--crocus)"></div><p class="color-name-en">crocus</p><p class="color-name-de">krokus</p></div>

    <div class="swatch-card"><div class="swatch" style="--tone: var(--lila)"></div><p class="color-name-en">lila</p><p class="color-name-de">lila</p></div>
    <div class="swatch-card"><div class="swatch" style="--tone: var(--iris)"></div><p class="color-name-en">iris</p><p class="color-name-de">iris</p></div>
    <div class="swatch-card"><div class="swatch" style="--tone: var(--azalea)"></div><p class="color-name-en">azalea</p><p class="color-name-de">azalea</p></div>
    <div class="swatch-card"><div class="swatch" style="--tone: var(--mulberry)"></div><p class="color-name-en">mulberry</p><p class="color-name-de is-bold">mulberry</p></div>

    <div class="swatch-card"><div class="swatch" style="--tone: var(--orange)"></div><p class="color-name-en">orange</p><p class="color-name-de">orange</p></div>
    <div class="swatch-card"><div class="swatch" style="--tone: var(--lipstic)"></div><p class="color-name-en">lipstic</p><p class="color-name-de">lipstic</p></div>
    <div class="swatch-card"><div class="swatch" style="--tone: var(--rosso)"></div><p class="color-name-en">rosso</p><p class="color-name-de">rosso</p></div>
    <div class="swatch-card"><div class="swatch" style="--tone: var(--salmon)"></div><p class="color-name-en">salmon</p><p class="color-name-de">salmon</p></div>

    <div class="swatch-card"><div class="swatch" style="--tone: var(--beige)"></div><p class="color-name-en">beige</p><p class="color-name-de">beige</p></div>
    <div class="swatch-card"><div class="swatch" style="--tone: var(--nugat)"></div><p class="color-name-en">nugat</p><p class="color-name-de">nugat</p></div>
    <div class="swatch-card"><div class="swatch" style="--tone: var(--kakao)"></div><p class="color-name-en">kakao</p><p class="color-name-de">kakao</p></div>
    <div class="swatch-card"><div class="swatch" style="--tone: var(--berry)"></div><p class="color-name-en">berry</p><p class="color-name-de">berry</p></div>

    <div class="swatch-card"><div class="swatch" style="--tone: var(--kiwi)"></div><p class="color-name-en">kiwi</p><p class="color-name-de">kiwi</p></div>
    <div class="swatch-card"><div class="swatch" style="--tone: var(--lipstic-green)"></div><p class="color-name-en">lipstic</p><p class="color-name-de">lipstic</p></div>
    <div class="swatch-card"><div class="swatch" style="--tone: var(--verde)"></div><p class="color-name-en">verde</p><p class="color-name-de">verde</p></div>
    <div class="swatch-card"><div class="swatch" style="--tone: var(--grass)"></div><p class="color-name-en">grass</p><p class="color-name-de">grass</p></div>

    <div class="swatch-card"><div class="swatch" style="--tone: var(--lazur)"></div><p class="color-name-en">lazur</p><p class="color-name-de">lazur</p></div>
    <div class="swatch-card"><div class="swatch" style="--tone: var(--turquoise)"></div><p class="color-name-en">turquoise</p><p class="color-name-de">turkis</p></div>
    <div class="swatch-card"><div class="swatch" style="--tone: var(--lagoon)"></div><p class="color-name-en">lagoon</p><p class="color-name-de">lagoon</p></div>
    <div class="swatch-card"><div class="swatch" style="--tone: var(--jeans)"></div><p class="color-name-en">jeans</p><p class="color-name-de">jeans</p></div>
  </section>
</main>
</body>
</html>
```